Business Law Firm Podcast Cover Art

Legal podcast seeking a redesign of our current podcast cover art to match better with our current business' brand profile. You can see our firm's site here: https://www.vorendlegal.com/ And I'm attaching our current podcast cover art. These are based on older photos as well, the newer versions are also attached.

Target Market(s)

business owners

Font styles to use
Serif
Sans Serif

Colors

Designer to choose colors to be used in the design.

Requirements
Must have
• Must have the title "Counsel Clear | Bright Venture".
Nice to have
• Photos of the hosts (Toren & Glen) would be nice, but we are not tied to it.
Should not have
• too small print

```html
<!DOCTYPE html>
<html lang="en">
<head>
<meta charset="UTF-8">
<title>Counsel Clear | Bright Venture Podcast</title>
<link href="https://fonts.googleapis.com/css2?family=Montserrat:wght@500;600;700&display=swap" rel="stylesheet">
<style>
  :root {
    --sky: #2ba3dc;
    --steel: #1d6e9f;
    --navy: #0c2b47;
    --ink: #050a10;
    --white: #ffffff;
    --title-mid: #1f5f86;
    --photo-dark: #161616;
  }
  html, body {
    margin: 0;
    padding: 0;
    overflow: hidden;
    background: var(--ink);
  }
  .cover {
    position: relative;
    width: 1200px;
    height: 1200px;
    overflow: hidden;
    font-family: "Montserrat", sans-serif;
    background:
      radial-gradient(circle at 100% 10%, var(--sky) 0%, rgba(43,163,220,0.55) 30%, rgba(29,110,159,0) 65%),
      linear-gradient(180deg, var(--steel) 0%, var(--navy) 55%, var(--ink) 100%);
  }
  .cover::after {
    content: "";
    position: absolute;
    inset: 0;
    background: linear-gradient(180deg, rgba(5,10,16,0) 70%, rgba(5,10,16,0.8) 100%);
    pointer-events: none;
    z-index: 2;
  }
  .frame {
    position: absolute;
    left: 38px;
    top: 38px;
    width: 1110px;
    height: 1110px;
    border: 7px solid var(--white);
    z-index: 3;
  }
  .title-art {
    position: absolute;
    left: 0;
    top: 0;
    width: 1200px;
    height: 460px;
    z-index: 4;
  }
  .title-top {
    font-family: "Montserrat", sans-serif;
    font-weight: 600;
    font-size: 104px;
    fill: var(--white);
  }
  .title-main {
    font-family: "Montserrat", sans-serif;
    font-weight: 700;
    font-size: 96px;
  }
  .podcast-label {
    font-family: "Montserrat", sans-serif;
    font-weight: 700;
    font-size: 44px;
    fill: var(--title-mid);
  }
  .mic-badge {
    position: absolute;
    left: 498px;
    top: 498px;
    width: 204px;
    height: 204px;
    z-index: 4;
  }
  .host-photo {
    position: absolute;
    top: 556px;
    height: 644px;
    z-index: 1;
    background: linear-gradient(180deg, rgba(150,150,150,0.35) 0%, rgba(110,110,110,0.55) 20%, rgba(40,40,40,0.9) 55%, var(--photo-dark) 100%);
  }
  .host-photo.left {
    left: 0;
    width: 480px;
    border-radius: 200px 200px 0 0;
  }
  .host-photo.right {
    left: 700px;
    width: 500px;
    border-radius: 200px 200px 0 0;
  }
</style>
</head>
<body>
  <div class="cover">
    <div class="host-photo left" role="img" aria-label="Black and white portrait of the first host in a dark suit and tie, smiling"></div>
    <div class="host-photo right" role="img" aria-label="Black and white portrait of the second host in a dark suit and tie, smiling"></div>

    <div class="frame"></div>

    <svg class="title-art" viewBox="0 0 1200 460" xmlns="http://www.w3.org/2000/svg">
      <defs>
        <linearGradient id="titleFill" x1="0" y1="0" x2="1" y2="0">
          <stop offset="0" stop-color="#0b2236"/>
          <stop offset="0.6" stop-color="#14405f"/>
          <stop offset="1" stop-color="#2a7fae"/>
        </linearGradient>
        <linearGradient id="labelBand" x1="0" y1="0" x2="1" y2="0">
          <stop offset="0" stop-color="#ffffff" stop-opacity="0"/>
          <stop offset="0.2" stop-color="#ffffff" stop-opacity="0.9"/>
          <stop offset="0.8" stop-color="#ffffff" stop-opacity="0.9"/>
          <stop offset="1" stop-color="#ffffff" stop-opacity="0"/>
        </linearGradient>
      </defs>
      <polyline points="150,146 86,146 86,282 106,282" fill="none" stroke="#ffffff" stroke-width="7"/>
      <polyline points="1050,146 1114,146 1114,282 1094,282" fill="none" stroke="#ffffff" stroke-width="7"/>

      <text class="title-top" x="164" y="184" textLength="872" lengthAdjust="spacingAndGlyphs">COUNSEL CLEAR</text>

      <rect x="106" y="216" width="988" height="120" fill="#ffffff"/>
      <text class="title-main" x="156" y="311" textLength="888" lengthAdjust="spacingAndGlyphs" fill="url(#titleFill)">BRIGHT VENTURE</text>

      <rect x="408" y="358" width="384" height="70" fill="url(#labelBand)"/>
      <text class="podcast-label" x="454" y="409" textLength="292" lengthAdjust="spacingAndGlyphs">PODCAST</text>
    </svg>

    <svg class="mic-badge" viewBox="0 0 180 180" xmlns="http://www.w3.org/2000/svg" role="img" aria-label="Microphone icon">
      <circle cx="90" cy="90" r="82" fill="none" stroke="#ffffff" stroke-width="8"/>
      <rect x="73" y="42" width="34" height="58" rx="17" fill="#ffffff"/>
      <g stroke="#1c4f72" stroke-width="3">
        <line x1="76" y1="56" x2="104" y2="56"/>
        <line x1="74" y1="64" x2="106" y2="64"/>
        <line x1="74" y1="72" x2="106" y2="72"/>
        <line x1="74" y1="80" x2="106" y2="80"/>
      </g>
      <path d="M62 86 a28 28 0 0 0 56 0" fill="none" stroke="#ffffff" stroke-width="5"/>
      <line x1="90" y1="114" x2="90" y2="134" stroke="#ffffff" stroke-width="5"/>
      <line x1="74" y1="136" x2="106" y2="136" stroke="#ffffff" stroke-width="5" stroke-linecap="round"/>
    </svg>
  </div>
</body>
</html>
```